Werbe Flyer an Hausbesitzer
Zielgruppe
Wir sind ein Immobilien Makler in Zürich. Wir werden den Werbe-Flyer zusammen mit einem Begleitschreiben und einem Rückantwort-Briefumschlag an Hausbesitzer per Post senden.
Zielgruppe:
ältere Leute, die Ihr Haus oder Wohnung verkaufen möchten.
Ziel:
Wir möchten den Maklerauftrag bekommen
Aufgabenstellung
Ein Werbe-Flyer erstellen.
Format:
A5
4 Seiten (Also A4 quer einmal gefaltet)
Hochformat
ein Beispiel liegt bei.
Der Text ist bereits definitiv.
Bilder und Layout ist frei wählbar.
Letzte Seite sollte abgetrennt werden können für die Rücksendung
Unsere Webpage als Info evtl. für Layout:
www.velaro-haus.ch

```html
<!DOCTYPE html>
<html lang="de">
<head>
<meta charset="utf-8">
<title>Velaro Haus AG – Flyer</title>
<link href="https://fonts.googleapis.com/css2?family=Lato:ital,wght@0,300;0,400;0,700;1,400&display=swap" rel="stylesheet">
<style>
  :root{
    --stage:#7b7b7b;
    --paper:#ffffff;
    --band-light:#f0f0f0;
    --band-dark:#cfcfcf;
    --navy:#1d3a7c;
    --ink:#3a3a3a;
    --rule:#8a8a8a;
    --sky:#8fb6dc;
    --green:#5e7a45;
    --stone:#c7bfb2;
    --suit:#2b2d33;
  }
  *{box-sizing:border-box;margin:0;padding:0}
  html,body{width:915px;height:1200px;overflow:hidden;background:var(--stage)}
  body{position:relative;font-family:"Lato",sans-serif;color:var(--ink)}
  .spread{position:absolute;left:67px;width:771px;height:545px;background:var(--paper);overflow:hidden}
  .spread--outer{top:35px}
  .spread--inner{top:620px}
  .abs{position:absolute}
  .header-band{position:absolute;left:0;top:0;height:91px;background:linear-gradient(90deg,var(--band-dark),var(--band-light) 60%,#e4e4e4)}
  .cover{position:absolute;left:380px;top:0;width:391px;height:545px;background:linear-gradient(100deg,#f4f4f4 0%,#e6e6e6 45%,#c9c9c9 100%)}
  .fold{position:absolute;left:380px;top:0;width:1px;height:545px;background:#d6d6d6}
  .brand{position:absolute;display:flex;align-items:center;gap:7px;color:var(--navy);font-weight:400;font-size:19px;letter-spacing:2px}
  .brand-mark{width:16px;height:16px;background:var(--navy)}
  .title{color:var(--navy);font-weight:300;text-transform:uppercase;font-size:19px;line-height:24px}
  .small{font-size:9px;font-weight:300}
  .lead{font-size:9.5px;color:var(--navy);font-weight:400}
  .check{position:absolute;left:79px;display:flex;align-items:center;gap:6px;font-size:10px;color:var(--navy);font-weight:300}
  .check-box{width:17px;height:17px;border:1px solid #9a9a9a}
  .field{position:absolute;left:79px;width:278px;border-top:1px solid var(--rule);padding-top:3px;font-size:9px;font-weight:300}
  .imprint{position:absolute;left:79px;top:491px;font-size:9.2px;font-weight:300;line-height:12.5px}
  .photo{position:absolute;width:165px;height:112px}
  .photo--house-a{background:linear-gradient(180deg,var(--sky) 0%,#cfd8df 45%,#d9cdb2 60%,var(--green) 100%)}
  .photo--house-b{background:linear-gradient(180deg,var(--sky) 0%,#e9ecef 40%,#f2f2f2 70%,var(--green) 100%)}
  .photo--house-c{background:linear-gradient(180deg,#dfe6ee 0%,#f1f1ec 50%,#7e9a5e 85%,#a34a4a 100%)}
  .photo--block{background:linear-gradient(180deg,#b6cde3 0%,var(--stone) 50%,#7b9a5b 100%)}
  .url{position:absolute;left:414px;top:423px;font-size:18px;font-weight:300;color:var(--navy)}
  .cover-foot{position:absolute;left:414px;top:502px;font-size:11.5px;font-weight:300;color:var(--ink);white-space:nowrap}
  .quote{position:absolute;left:38px;top:182px;z-index:2;font-size:13px;line-height:18px;font-style:italic;color:#1a1a1a;white-space:nowrap}
  .team-photo{position:absolute;left:168px;top:154px;width:190px;height:231px;background:linear-gradient(180deg,#f5f5f5 0%,#e7e7ea 35%,var(--suit) 55%,#1c1d22 100%)}
  .contact-band{position:absolute;left:0;top:385px;width:381px;height:160px;background:linear-gradient(90deg,#d2d2d2,#f3f3f3)}
  .office-photo{position:absolute;left:0;top:445px;width:132px;height:100px;background:linear-gradient(180deg,#c9d3db 0%,#8e7a63 40%,#6f5c4a 75%,#6d7d5c 100%)}
  .consultants{position:absolute;left:144px;top:392px}
  .consultants h3{font-size:13.5px;font-weight:300;color:var(--navy);letter-spacing:.2px}
  .person{position:absolute;top:19px;font-size:9px;font-weight:300;white-space:nowrap;line-height:12px}
  .person strong{display:block;font-weight:700;color:var(--navy);font-size:9px}
  .office{position:absolute;left:144px;top:463px;font-size:9.5px;font-weight:300;line-height:13.5px}
  .service{position:absolute;left:415px;width:330px}
  .service h2{font-size:13.5px;font-weight:300;color:var(--navy);text-transform:uppercase;margin-bottom:5px}
  .service p{margin-left:16px;font-size:10.1px;line-height:14.1px;font-weight:300;color:#2e2e2e}
</style>
</head>
<body>

<section class="spread spread--outer">
  <div class="header-band" style="width:380px"></div>
  <div class="cover"></div>
  <div class="fold"></div>

  <!-- Reply card -->
  <div class="brand" style="left:40px;top:36px"><span class="brand-mark"></span>VELARO HAUS AG</div>
  <h1 class="title abs" style="left:38px;top:112px">Rückantwort</h1>
  <p class="small abs" style="left:79px;top:150px">Einfach abtrennen und im beigefügten Rückumschlag an uns senden</p>
  <p class="lead abs" style="left:79px;top:174px">Bitte kreuzen Sie Ihre Wünsche an.</p>
  <p class="lead abs" style="left:79px;top:201px">Ja, wir möchten …</p>
  <label class="check" style="top:226px"><span class="check-box"></span>… unsere Immobilie verkaufen</label>
  <label class="check" style="top:258px"><span class="check-box"></span>… eine Immobilie kaufen</label>
  <label class="check" style="top:290px"><span class="check-box"></span>… ein persönliches Gespräch</label>
  <div class="field" style="top:341px">Name/Vorname</div>
  <div class="field" style="top:372px">Strasse</div>
  <div class="field" style="top:404px">PLZ/Ort</div>
  <div class="field" style="top:435px">Telefon</div>
  <div class="field" style="top:466px">E-Mail</div>
  <p class="imprint">VELARO HAUS AG | LINDENWEG 12 | 8006 ZÜRICH<br>Fax 044 000 11 25 | info@velaro-haus.ch | www.velaro-haus.ch</p>
  <svg class="abs" style="left:369px;top:506px" width="14" height="18" viewBox="0 0 14 18" aria-hidden="true">
    <g fill="none" stroke="#444" stroke-width="1">
      <line x1="3" y1="1" x2="10" y2="13"/><line x1="11" y1="1" x2="4" y2="13"/>
      <circle cx="3.5" cy="15" r="2"/><circle cx="10.5" cy="15" r="2"/>
    </g>
  </svg>

  <!-- Cover -->
  <div class="brand" style="left:414px;top:36px"><span class="brand-mark"></span>VELARO HAUS AG</div>
  <h1 class="title abs" style="left:585px;top:112px;font-size:20px">Immobilien<br>sind unsere<br>Leidenschaft</h1>
  <div class="photo photo--house-a" style="left:414px;top:154px" role="img" aria-label="Foto: Einfamilienhaus mit Terrasse am Hang"></div>
  <div class="photo photo--house-b" style="left:414px;top:272px" role="img" aria-label="Foto: weisses Einfamilienhaus mit dunklem Dach"></div>
  <div class="photo photo--house-c" style="left:585px;top:209px;width:166px" role="img" aria-label="Foto: Wohnhaus mit grünen Fensterläden und Garten"></div>
  <div class="photo photo--block" style="left:585px;top:328px;width:166px" role="img" aria-label="Foto: modernes Mehrfamilienhaus mit Rasen"></div>
  <p class="url">www.velaro-haus.ch</p>
  <p class="cover-foot">VELARO HAUS AG | LINDENWEG 12 | 8006 ZÜRICH</p>
</section>

<section class="spread spread--inner">
  <div class="header-band" style="width:771px"></div>
  <div class="brand" style="left:40px;top:36px"><span class="brand-mark"></span>VELARO HAUS AG</div>

  <h1 class="title abs" style="left:39px;top:101px">Ihre Partner für alle Fragen<br>rund um Ihre Immobilie</h1>
  <div class="contact-band"></div>
  <div class="team-photo" role="img" aria-label="Foto: die beiden Berater im Anzug, stehend"></div>
  <p class="quote">„Wir setzen uns für<br>&nbsp;jede Liegenschaft<br>&nbsp;ein, als wäre es<br>&nbsp;unsere Eigene.“</p>
  <div class="office-photo" role="img" aria-label="Foto: Geschäftshaus des Büros"></div>

  <div class="consultants">
    <h3>THE CREATIVE CONSULTANTS</h3>
    <p class="person" style="left:1px"><strong>MARC-ANDRÉ KELLER</strong>Tel. direkt 044 000 11 24</p>
    <p class="person" style="left:116px"><strong>THOMAS B. WYSS</strong>Tel. direkt 044 000 11 21</p>
  </div>
  <p class="office">VELARO HAUS AG<br>Lindenweg 12 | 8006 Zürich<br>Tel. 044 000 11 20 | Fax 044 000 11 25<br>info@velaro-haus.ch | www.velaro-haus.ch</p>

  <div class="service" style="top:101px">
    <h2>Unsere Dienstleistungen</h2>
    <p>Der Kauf und Verkauf von Immobilien ist Vertrauenssache. Aus diesem Grund geniesst bei Velaro Haus AG die persönliche Beziehung zum Kunden neben allen fachlichen Aspekten in jeder Phase höchste Priorität. So behalten Sie stets den Überblick und bleiben in jeder Phase auf dem Laufenden.</p>
  </div>
  <div class="service" style="top:208px">
    <h2>Schätzung</h2>
    <p>Es gibt viele Gründe, sich auch ohne Verkaufsabsichten hin und wieder über den Wert seiner eigenen Immobilie zu informieren. Wir übernehmen für Sie auf Wunsch die genaue und objektive Wertbeurteilung von Einfamilienhaus und Grundstück.</p>
  </div>
  <div class="service" style="top:301px">
    <h2>Verkauf</h2>
    <p>Ist ein Verkauf geplant, überprüfen wir für Sie im Vorfeld die aktuellen Verkaufsmöglichkeiten. Dazu gehören sowohl die Ermittlung eines realistischen Verkaufspreises als auch die Erstellung detaillierter Verkaufsunterlagen. Auch Objektbesichtigungen führen wir für Sie durch.</p>
  </div>
  <div class="service" style="top:411px">
    <h2>Beurkundung und Übertragung</h2>
    <p>Neben Schätzung Ihrer Liegenschaft und Marketing führen wir für Sie auch die Preisverhandlungen mit potentiellen Interessenten. Zudem erstellen wir mit dem zuständigen Notariat den Entwurf und die Ausarbeitung der Kaufverträge und begleiten Sie bis zur Beurkundung und Eigentumsübertragung auf dem Grundbuchamt.</p>
  </div>
</section>

</body>
</html>
```